Business Card for a Jewellery Brand

Business card for an upscale jewellery brand. Attached is the brand logo and icon and color board. I am looking for two card versions: one for the founder and one is generic. The card should be elegant and convey upscale and premium feel. I am open to both square and rectangle card shapes.

Industry/Entity Type

Jewelry

Contact Information for Business Card

Two cards: (1) Suneha Parmeshwar (Founder) (2) General
(1) Suneha Parmeshwar card should have Name: Suneha Parmeshwar, Title: Founder Email id: suneha@quelm.com.au. Phone no: +61452190437
(2) Generic card should have Email id: info@quelm.com.au. Phone no: +61431267508

Requirements
Must have
• Workmark
• ICON
• Phone no
• Email ID
• ABN: 48291175034 (Note: ABN is Business number in Australia)
• Website: www.quelm.com.au
• Instagram: quelm_jewellery
• Facebook: @quelmjewellery
Nice to have
• Tagline

```html
<!DOCTYPE html>
<html lang="en">
<head>
<meta charset="utf-8">
<title>QUELM business cards</title>
<link rel="stylesheet" href="https://fonts.googleapis.com/css2?family=Open+Sans:wght@300;400;600;700&display=swap">
<style>
  :root {
    --backdrop: #3a3330;
    --card: #141414;
    --card-edge: #1d1d1d;
    --silver: #8d8d8d;
    --silver-soft: #5e5e5e;
    --rose: #e8a39a;
    --ink-light: #f2f2f2;
  }
  * { box-sizing: border-box; margin: 0; padding: 0; }
  html, body { width: 1200px; height: 864px; overflow: hidden; }
  body {
    background: var(--backdrop);
    font-family: "Open Sans", Arial, sans-serif;
    position: relative;
  }
  .card {
    position: absolute;
    width: 520px;
    height: 298px;
    background: var(--card);
    border: 1px solid var(--card-edge);
    box-shadow: 0 18px 40px rgba(0,0,0,.45);
  }

  /* Front: wordmark and tagline */
  .card-front { left: 70px; top: 130px; }
  .front-wordmark {
    position: absolute;
    left: 0; right: 0; top: 96px;
    text-align: center;
    font-weight: 300;
    font-size: 54px;
    letter-spacing: 22px;
    padding-left: 22px;
    color: var(--silver);
  }
  .front-rule {
    position: absolute;
    left: 60px; right: 60px; top: 190px;
    height: 1px;
    background: linear-gradient(90deg, transparent, var(--silver) 20%, var(--silver) 80%, transparent);
  }
  .tagline {
    position: absolute;
    left: 0; right: 0; top: 198px;
    text-align: center;
    font-size: 12px;
    letter-spacing: 1px;
    color: var(--silver);
  }

  /* Back: founder details */
  .card-back { left: 610px; top: 420px; }
  .back-wordmark {
    position: absolute;
    left: 40px; top: 124px;
    font-weight: 400;
    font-size: 38px;
    letter-spacing: 6px;
    color: var(--rose);
  }
  .back-divider {
    position: absolute;
    left: 262px; top: 52px;
    width: 1px; height: 190px;
    background: linear-gradient(180deg, transparent, #cfcfcf 25%, #cfcfcf 75%, transparent);
  }
  .contact-block {
    position: absolute;
    left: 282px; top: 56px;
    color: var(--ink-light);
    font-size: 14px;
    line-height: 19px;
  }
  .person-name { color: var(--rose); font-weight: 700; font-size: 15px; }
  .person-meta { margin-bottom: 6px; }
  .contact-list { list-style: none; }
  .contact-list li { display: flex; align-items: center; gap: 9px; }
  .contact-icon { width: 11px; height: 11px; flex: none; }
  .contact-icon.square { background: var(--ink-light); border-radius: 2px; width: 10px; height: 10px; }
</style>
</head>
<body>

  <section class="card card-front" aria-label="Card front">
    <div class="front-wordmark">QUELM</div>
    <div class="front-rule"></div>
    <p class="tagline">LOVE IS IN THE AIR</p>
  </section>

  <section class="card card-back" aria-label="Card back">
    <div class="back-wordmark">QUELM</div>
    <div class="back-divider"></div>
    <div class="contact-block">
      <p class="person-name">Suneha Parmeshwar</p>
      <p>Founder</p>
      <p class="person-meta">ABN: 48291175034</p>
      <ul class="contact-list">
        <li>
          <svg class="contact-icon" viewBox="0 0 12 12" aria-hidden="true"><rect x="3" y="0.5" width="6" height="11" rx="1" fill="none" stroke="#f2f2f2"/><rect x="5" y="9" width="2" height="1" fill="#f2f2f2"/></svg>
          +61452190437
        </li>
        <li>
          <svg class="contact-icon" viewBox="0 0 12 12" aria-hidden="true"><rect x="0.5" y="2.5" width="11" height="7" fill="#f2f2f2"/><path d="M0.5 2.5 L6 7 L11.5 2.5" fill="none" stroke="#141414"/></svg>
          suneha@quelm.com.au
        </li>
        <li>
          <svg class="contact-icon" viewBox="0 0 12 12" aria-hidden="true"><circle cx="6" cy="6" r="5.5" fill="#f2f2f2"/><path d="M0.5 6 H11.5 M6 0.5 C3 3 3 9 6 11.5 C9 9 9 3 6 0.5" fill="none" stroke="#141414" stroke-width=".8"/></svg>
          www.quelm.com.au
        </li>
        <li><span class="contact-icon square"></span>quelm_jewellery</li>
        <li><span class="contact-icon square"></span>@quelmjewellery</li>
      </ul>
    </div>
  </section>

</body>
</html>
```